Patient Satisfaction

We are extending our social listening and intelligence platform for Physicians to patient satisfaction app. Our platform monitors social media and review sites and collects, classifies and distilled patient satisfaction into nine Categories - Thoroughness, Answers Q's, Collaborative, Caring, Time Spent, Previous Success, Instruction Clarity, Follow-up and Reputation

The app will have three main states: (1) Home state showing the metric for each category, (2) a detailed page for each Category showing the metric, topics discussed and sites sourced, (3) Leaderboard showing Physicians with best scores.

If you follow our wireframes, please take liberty to extend it. We like the Panelo 6 tiles, but our wireframes fall far short of meeting its coolness and usefulness. For example, we don't have different size tiles, and would live them, or content on the tiles to make them more meaningful. [Note: use KV instead of GLH.]
Updates

The designs submitted to date look great, but they reminded me that my instructions were unclear. Feel free to follow the wireframes if you like the UI, but we also welcome your thoughts on UI in addition to look and feel. If you follow our wireframes, please take liberty to extend it. We like the Panelo 6 tile, but our wireframes falls far short of meeting its coolness and usefulness. For example, we don't have different size tiles or content on the tiles to make them more meaningful. If you've submitted designs, please feel free to revise them or submit a different look. And if you haven't submitted designs, please feel free to give us your best thoughts on UI and design.

Target Market(s)

US Physicians

Industry/Entity Type

Media

Font styles to use
Sans Serif

Colors
f37022
5c5c5c
33a6d7

Requirements
Must have
• Home state
Visual icons
Nice to have
• Leaderbaord

```html
<!DOCTYPE html>
<html lang="en">
<head>
<meta charset="utf-8">
<title>Dr. Ben Carver – Patient Satisfaction</title>
<link rel="stylesheet" href="https://fonts.googleapis.com/css2?family=Open+Sans:wght@300;400;600;700&display=swap">
<style>
  :root{
    --amber:#ffb300;
    --amber-dark:#f7a600;
    --orange-top:#ffa614;
    --orange-bottom:#ff9000;
    --blue-top:#2f8be9;
    --blue-bottom:#1f62df;
    --grid-bg:#efefef;
    --tile-shadow:#c9c9c9;
    --tabbar:#1b1b1b;
    --tab-line:#c98a00;
    --tab-text:#f6a800;
    --white:#ffffff;
    --photo-a:#c9b8ad;
    --photo-b:#e9e2dc;
    --face:#d8b9a2;
  }
  *{box-sizing:border-box;margin:0;padding:0}
  html,body{width:676px;height:1200px;overflow:hidden;background:var(--grid-bg)}
  body{font-family:"Open Sans",Arial,sans-serif;color:var(--white);position:relative}
  .app{position:relative;width:676px;height:1200px;overflow:hidden}

  .hero{position:absolute;left:0;top:0;width:676px;height:254px;
    background:linear-gradient(120deg,var(--photo-a) 0%,var(--photo-b) 55%,#b99e92 100%)}
  .hero-title{position:absolute;left:0;right:0;top:62px;text-align:center;font-size:36px;font-weight:400;letter-spacing:.3px;text-shadow:0 1px 3px rgba(0,0,0,.25)}
  .round-btn{position:absolute;top:53px;width:64px;height:64px;border-radius:50%;background:var(--amber);display:flex;align-items:center;justify-content:center}
  .menu-btn{left:21px}
  .bell-btn{left:584px}

  .stats-band{position:absolute;left:0;top:254px;width:676px;height:108px;background:var(--amber)}
  .stat{position:absolute;top:0;height:108px;text-align:center;font-size:32px;font-weight:400}
  .stat b{font-weight:700}
  .stat svg{display:block;margin:14px auto 2px}
  .stat-rank{left:48px;width:180px}
  .stat-comment{left:428px;width:222px}

  .avatar{position:absolute;left:245px;top:167px;width:186px;height:186px;border-radius:50%;border:8px solid var(--white);
    background:radial-gradient(circle at 50% 40%,var(--face) 0%,#c8a58c 45%,#e8eef3 46%,#dfe6ec 100%)}

  .tile{position:absolute;box-shadow:0 5px 0 var(--tile-shadow);overflow:hidden}
  .tile.blue{background:linear-gradient(160deg,var(--blue-top),var(--blue-bottom))}
  .tile.orange{background:linear-gradient(180deg,var(--orange-top),var(--orange-bottom))}
  .tile.amber{background:var(--amber)}
  .tile-label{position:absolute;left:23px;bottom:22px;font-size:34px;font-weight:400}
  .tile-label.small{left:0;right:0;bottom:8px;text-align:center;font-size:24px}

  .social-index{left:12px;top:375px;width:321px;height:338px}
  .social-index .score{position:absolute;left:0;right:0;top:20px;text-align:center;font-size:180px;font-weight:300;line-height:1.2}
  .bedside{left:344px;top:375px;width:151px;height:158px}
  .knowledge{left:507px;top:375px;width:156px;height:158px}
  .outcome{left:344px;top:545px;width:319px;height:168px}
  .time-spent{left:12px;top:725px;width:321px;height:338px}
  .review{left:344px;top:725px;width:319px;height:338px}
  .tile-icon{position:absolute;left:0;right:0;margin:auto;display:block}

  .review-head{position:absolute;left:22px;right:22px;top:18px;display:flex;justify-content:space-between;align-items:baseline}
  .review-source{font-size:25px}
  .review-date{font-size:18px}
  .review-body{position:absolute;left:22px;right:22px;top:68px;font-size:18px;line-height:1.33;text-align:justify;font-weight:400}
  .review .tile-label{font-size:33px;bottom:14px}

  .tabbar{position:absolute;left:0;top:1073px;width:676px;height:127px;background:var(--tabbar);display:flex;border-top:1px solid var(--tab-line)}
  .tab{flex:1;text-align:center;color:var(--tab-text);font-size:18px;font-weight:600;letter-spacing:1.2px}
  .tab+.tab{border-left:1px solid var(--tab-line)}
  .tab svg{display:block;margin:22px auto 14px}
</style>
</head>
<body>
<main class="app">
  <header class="hero" role="img" aria-label="Photo of a physician examining an infant with a stethoscope">
    <a class="round-btn menu-btn" aria-label="Menu">
      <svg width="30" height="22" viewBox="0 0 30 22"><g fill="#fff"><rect y="0" width="30" height="3" rx="1.5"/><rect y="9.5" width="30" height="3" rx="1.5"/><rect y="19" width="30" height="3" rx="1.5"/></g></svg>
    </a>
    <h1 class="hero-title">Dr. Ben Carver</h1>
    <a class="round-btn bell-btn" aria-label="Notifications">
      <svg width="28" height="30" viewBox="0 0 28 30"><path fill="#fff" d="M14 2c-5 0-8 4-8 9v7l-3 4h22l-3-4v-7c0-5-3-9-8-9z"/><circle cx="14" cy="25" r="3.5" fill="#fff"/></svg>
    </a>
  </header>

  <section class="stats-band">
    <div class="stat stat-rank">
      <svg width="40" height="38" viewBox="0 0 40 38"><path fill="none" stroke="#fff" stroke-width="2.5" d="M4 36 L12 4"/><path fill="#fff" d="M12 4c6-3 10 3 18 0l8 2-6 14c-8 3-12-3-18 0z"/></svg>
      Rank: <b>5/15</b>
    </div>
    <div class="stat stat-comment">
      <svg width="40" height="38" viewBox="0 0 40 38"><path fill="#fff" d="M20 2C10 2 2 9 2 18c0 4 2 8 5 10l-2 8 9-5c2 .5 4 1 6 1 10 0 18-7 18-16S30 2 20 2z"/></svg>
      Comment: <b>22</b>
    </div>
  </section>

  <div class="avatar" role="img" aria-label="Profile photo of the physician"></div>

  <section class="tile blue social-index">
    <div class="score">72</div>
    <div class="tile-label">Social Index</div>
  </section>

  <section class="tile amber bedside">
    <svg class="tile-icon" style="top:30px" width="84" height="62" viewBox="0 0 84 62"><g fill="none" stroke="#fff" stroke-width="4"><path d="M4 4v50M80 20v34M4 38h76M4 46h76"/><circle cx="8" cy="56" r="4"/><circle cx="76" cy="56" r="4"/></g><circle cx="20" cy="26" r="6" fill="#fff"/><rect x="30" y="22" width="40" height="12" rx="5" fill="#fff"/></svg>
    <div class="tile-label small">Bedside</div>
  </section>

  <section class="tile amber knowledge">
    <svg class="tile-icon" style="top:26px" width="72" height="68" viewBox="0 0 72 68"><g fill="none" stroke="#fff" stroke-width="4" stroke-linejoin="round"><path d="M36 12C28 5 14 4 4 8v52c10-4 24-3 32 4 8-7 22-8 32-4V8C58 4 44 5 36 12z"/><path d="M36 12v52"/><path d="M12 22h16M12 32h16M12 42h16M44 22h16M44 32h16M44 42h16"/></g></svg>
    <div class="tile-label small">Knowledge</div>
  </section>

  <section class="tile blue outcome">
    <svg class="tile-icon" style="top:24px" width="72" height="66" viewBox="0 0 72 66"><path fill="#fff" d="M36 64C16 48 2 36 2 20 2 9 10 2 19 2c7 0 13 4 17 10 4-6 10-10 17-10 9 0 17 7 17 18 0 16-14 28-34 44z"/><path fill="none" stroke="#2a7ae7" stroke-width="3.5" stroke-linejoin="round" d="M4 34h18l5-10 7 22 6-28 5 16h23"/></svg>
    <div class="tile-label">Outcome</div>
  </section>

  <section class="tile orange time-spent">
    <svg class="tile-icon" style="top:66px" width="150" height="150" viewBox="0 0 150 150"><circle cx="75" cy="75" r="67" fill="none" stroke="#fff" stroke-width="9"/><path d="M75 30v45l30 26" fill="none" stroke="#fff" stroke-width="8" stroke-linecap="round" stroke-linejoin="round"/></svg>
    <div class="tile-label">Time Spent</div>
  </section>

  <section class="tile blue review">
    <div class="review-head"><span class="review-source">Revuu</span><span class="review-date">July 6,2014</span></div>
    <p class="review-body">Super nice lady, she reminds me of my mother. I have been to three cardiologists in town and she is easily the best of the three. She offers a good combination of clinical and "off the cuff" advice. Highly recommended.</p>
    <div class="tile-label">Recent Review</div>
  </section>

  <nav class="tabbar">
    <div class="tab">
      <svg width="40" height="40" viewBox="0 0 40 40"><path fill="none" stroke="#f6a800" stroke-width="2.5" d="M4 38 L12 4"/><path fill="#f6a800" d="M12 4c6-3 10 3 18 0l8 2-6 14c-8 3-12-3-18 0z"/></svg>
      RANKING
    </div>
    <div class="tab">
      <svg width="40" height="40" viewBox="0 0 40 40"><g fill="#f6a800"><circle cx="8" cy="8" r="4"/><circle cx="20" cy="6" r="5"/><circle cx="32" cy="8" r="4"/><rect x="2" y="14" width="10" height="16" rx="3"/><rect x="14" y="13" width="12" height="20" rx="3"/><rect x="28" y="14" width="10" height="16" rx="3"/><rect x="16" y="30" width="8" height="10"/></g></svg>
      FOLLOWING
    </div>
    <div class="tab">
      <svg width="40" height="40" viewBox="0 0 40 40"><g fill="#f6a800"><circle cx="20" cy="6" r="5"/><rect x="13" y="13" width="14" height="18" rx="3"/><rect x="15" y="28" width="10" height="12"/></g></svg>
      FOLLOWERS
    </div>
  </nav>
</main>
</body>
</html>
```